Real Estate Web Design

Hi

We are a real estate agency who is looking for a Corporate Design that would match our Style Guide. We have already developed the website but we want to apply our Branding on top of it. I am looking for some creative concepts

Below is our Test link for our new website
http://brightkeyhomes.sampledemo.com.au/

Attached is our Style Guide

Cheers
Ruvo

Industry/Entity Type

Real Estate

```html
<!DOCTYPE html>
<html lang="en">
<head>
<meta charset="utf-8">
<title>Brightkey Homes Management</title>
<link href="https://fonts.googleapis.com/css2?family=Arimo:ital,wght@0,400;0,700;1,700&family=Open+Sans:wght@400;600&display=swap" rel="stylesheet">
<style>
:root{
  --navy:#0d2d57;
  --blue:#0b55a3;
  --blue-deep:#0a4c97;
  --red:#e8312a;
  --sky:#dfe8f3;
  --page:#f2f2f2;
  --ink:#222;
  --photo-warm:#b98a62;
  --photo-house:#8ea3b3;
  --orange:#f0962e;
}
*{box-sizing:border-box;margin:0;padding:0}
html,body{width:702px;height:1200px;overflow:hidden;background:var(--page)}
body{font-family:"Arimo",Arial,sans-serif;color:var(--ink)}
.site{position:relative;width:800px;height:1367px;transform:scale(0.8775);transform-origin:0 0;background:var(--page)}
.abs{position:absolute}
/* top bar */
.topbar{left:0;top:0;width:800px;height:22px;background:var(--navy)}
.topbar .email{left:62px;top:5px;font:10px "Open Sans",sans-serif;color:#c9d6e8}
.social{right:48px;top:0;display:flex}
.social span{width:25px;height:22px;border-left:1px solid #24466f;display:flex;align-items:center;justify-content:center}
.social span i{width:8px;height:8px;background:#c9d6e8;display:block}
/* header */
.header{left:0;top:22px;width:800px;height:96px;background:linear-gradient(#fff,#cdd9ee)}
.brand{left:44px;top:10px;display:flex;align-items:center;gap:8px}
.brand .mark{width:22px;height:22px;background:var(--red)}
.brand .name{font:700 22px "Arimo",sans-serif;color:var(--red);line-height:1.05}
.callout{right:102px;top:18px;text-align:right}
.callout .lead{font:italic 700 14px "Arimo",sans-serif;color:var(--blue)}
.callout .lead em{color:var(--red)}
.callout .num{font:700 22px "Arimo",sans-serif;color:var(--navy);margin-top:2px}
.nav{left:43px;top:93px;width:706px;height:25px;background:var(--blue)}
.nav a{position:absolute;top:0;font:700 10px "Arimo",sans-serif;color:#fff;text-decoration:none;line-height:25px;white-space:nowrap}
.nav .sep{position:absolute;top:0;width:1px;height:25px;background:#2a6cb3}
.nav .welcome{left:547px;width:159px;height:25px;background:var(--red);font:400 15px "Arimo",sans-serif;padding-left:12px}
/* hero */
.hero{left:43px;top:118px;width:706px;height:277px;
  background:
    linear-gradient(180deg,rgba(255,255,255,0) 70%,rgba(150,150,150,.45) 100%),
    linear-gradient(90deg,#e4e2dc 0%,#d3cbbc 18%,#a4654a 30%,#8a4b36 40%,#2f2421 48%,#3a2b25 56%,#8d4f3a 64%,#9a5a42 72%,#c7c2bd 86%,#d9dee6 100%)}
.video{left:59px;top:305px;width:136px;height:78px;background:linear-gradient(#2c2c2c 0 16px,#e9d7a0 16px,#9fbd7a);border:2px solid #fff}
.search{left:541px;top:197px;width:216px;height:165px;background:#f3f3f3;border-top:3px solid var(--red);font:10px "Arimo",sans-serif;color:#333}
.search .row{position:absolute;left:0;width:216px;height:18px}
.search .lbl{position:absolute;right:150px;top:3px;white-space:nowrap}
.search .fld{position:absolute;left:76px;width:128px;height:18px;background:#fff;border:1px solid #bbb;padding:3px 5px;font-size:8px}
.search .small{width:26px}
.search .btn{position:absolute;left:76px;top:136px;width:77px;height:20px;background:var(--red);color:#fff;font:700 8px "Arimo",sans-serif;text-align:center;line-height:20px}
.stripe-r{left:0;top:395px;width:800px;height:4px;background:var(--red)}
.stripe-b{left:0;top:399px;width:800px;height:4px;background:var(--blue)}
/* content card */
.card{left:52px;top:430px;width:695px;height:613px;background:#fff;border:1px solid #e3e3e3}
.headline{left:52px;top:442px;width:695px;text-align:center;font:700 22px "Arimo",sans-serif;color:var(--blue-deep)}
.headline em{font-style:normal;color:var(--red)}
.band{left:53px;top:473px;width:693px;height:53px;background:linear-gradient(#eef3f9,var(--sky))}
.tab{height:25px;background:var(--red);color:#fff;font:700 12px "Arimo",sans-serif;line-height:25px;padding-left:9px;width:159px}
.pic{background:linear-gradient(135deg,#4a2c18,var(--photo-warm))}
.pic .cap{position:absolute;left:0;bottom:0;width:100%;height:44px;background:rgba(0,0,0,.5);color:#fff;font:12px "Arimo",sans-serif;padding:8px 8px}
.map{background:radial-gradient(circle at 45% 45%,#f6a544,var(--orange) 60%,#e8852a);border-radius:6px}
.blurb{font:12px/1.25 "Arimo",sans-serif;color:#333}
.more{font:9px "Arimo",sans-serif;color:var(--red)}
.sec{font:700 14px "Arimo",sans-serif;color:var(--blue-deep)}
.rule{height:1px;background:#f1b3b0}
.deal .img{width:90px;height:59px;background:linear-gradient(#6f9ed8 45%,var(--photo-house) 46%,#7f8f60)}
.deal .price{width:90px;height:22px;background:var(--red);color:#fff;font:9px "Arimo",sans-serif;line-height:22px;padding-left:6px;white-space:nowrap}
.deal .price b{font-weight:700}
.deal .spec{font:9px/1.2 "Arimo",sans-serif;color:#222;margin:4px 0 0 5px}
.deal .more{margin:7px 0 0 5px}
.quote{font:9px/1.25 "Arimo",sans-serif;color:#222;width:190px}
.by{font:9px "Arimo",sans-serif;color:var(--blue)}
.stars{display:flex;gap:1px}
.stars i{width:8px;height:8px;background:#f2b11f;display:block}
/* featured */
.feat-tab{left:77px;top:1019px;width:430px;height:24px;background:var(--red);color:#fff;font:700 12px "Arimo",sans-serif;line-height:24px;padding-left:10px}
.feat{left:52px;top:1043px;width:695px;height:145px;background:var(--blue-deep)}
.thumb{width:89px;height:59px;background:linear-gradient(#7fb0e2 40%,#9aa3a0 41%,#6c8a4a)}
.tcap{font:9px/1.2 "Arimo",sans-serif;color:#fff;width:110px;white-space:nowrap;margin-top:7px}
.arrow{width:20px;height:26px;background:var(--red);border-radius:3px;display:flex;align-items:center;justify-content:center}
.call{left:52px;top:1154px;width:695px;text-align:center;font:24px "Arimo",sans-serif;color:#fff}
/* footer */
.footer{left:47px;top:1197px;width:733px;height:140px;background:linear-gradient(#ececec 30%,#c9ccd0)}
.fcol h4{font:600 13px "Open Sans",sans-serif;color:#111;margin-bottom:8px}
.fcol p{font:8.5px/1.35 "Open Sans",sans-serif;color:#333}
.fline{left:62px;top:1336px;width:696px;height:1px;background:#cfcfcf}
.copy{font:7px "Open Sans",sans-serif;color:#333}
</style>
</head>
<body>
<div class="site">
  <div class="abs topbar">
    <div class="abs email">Email us at : info@brightkeyhomes.com.au</div>
    <div class="abs social"><span><i></i></span><span><i></i></span><span><i></i></span><span><i></i></span><span><i></i></span></div>
  </div>

  <header class="abs header">
    <div class="abs brand"><span class="mark"></span><span class="name">Brightkey Homes<br>Management</span></div>
    <div class="abs callout">
      <div class="lead">Just what you need <em>call us now</em></div>
      <div class="num">08 - 5550 - 1234</div>
    </div>
  </header>

  <nav class="abs nav">
    <a style="left:25px">HOME</a><span class="sep" style="left:65px"></span>
    <a style="left:77px">ABOUT US</a><span class="sep" style="left:137px"></span>
    <a style="left:150px">LAND LORDS</a><span class="sep" style="left:220px"></span>
    <a style="left:232px">TENANTS</a><span class="sep" style="left:287px"></span>
    <a style="left:300px">PROPERTIES</a><span class="sep" style="left:369px"></span>
    <a style="left:382px">CONTACT US</a><span class="sep" style="left:452px"></span>
    <a style="left:465px">TESTIMONIALS</a>
    <a class="welcome">WELCOME</a>
  </nav>

  <div class="abs hero" role="img" aria-label="Young couple receiving house keys from an agent on a brick porch"></div>
  <div class="abs video" role="img" aria-label="Animated video thumbnail of a neighbourhood"></div>

  <form class="abs search">
    <div class="row" style="top:12px"><span class="lbl">Property Type</span><span class="fld"></span></div>
    <div class="row" style="top:37px"><span class="lbl">Zip codes</span><span class="fld"></span></div>
    <div class="row" style="top:62px"><span class="lbl">Min Price</span><span class="fld">0</span></div>
    <div class="row" style="top:87px"><span class="lbl">Max Price</span><span class="fld">0</span></div>
    <div class="row" style="top:112px"><span class="lbl">Bedrooms</span><span class="fld small">0</span>
      <span style="position:absolute;left:123px;top:3px">Bathrooms</span><span class="fld small" style="left:178px">0</span></div>
    <div class="btn">Lis Properties</div>
  </form>

  <div class="abs stripe-r"></div><div class="abs stripe-b"></div>

  <main>
    <div class="abs card"></div>
    <h1 class="abs headline">WE ARE OFFERING THE <em>BEST REAL ESTATE DEALS</em></h1>
    <div class="abs band"></div>

    <div class="abs tab" style="left:86px;top:501px">Property Managed</div>
    <div class="abs tab" style="left:320px;top:501px">Land Lords</div>
    <div class="abs tab" style="left:548px;top:501px">Opportunities</div>

    <div class="abs pic" style="left:73px;top:538px;width:192px;height:98px" role="img" aria-label="Warm-lit architectural detail">
      <div class="cap">Do you want your<br>property managed?</div></div>
    <div class="abs pic" style="left:303px;top:538px;width:192px;height:98px;background:linear-gradient(135deg,#6a4630,#c9a07a)" role="img" aria-label="Smiling landlord portrait">
      <div class="cap">How much rent can I get<br>per week?</div></div>
    <div class="abs map" style="left:546px;top:537px;width:154px;height:130px" role="img" aria-label="Map of Australia showing franchise states"></div>

    <p class="abs blurb" style="left:74px;top:656px;width:190px">For the past 10 years in the South West we have been the leading specialist rental company.</p>
    <p class="abs blurb" style="left:304px;top:656px;width:195px">We have provided satisfaction to hundred's of landlords by getting the best tenant, paying the best rent in the shortest possible time.</p>
    <p class="abs blurb" style="left:546px;top:674px;width:154px;text-align:center">Franchise<br>Opportunities</p>
    <span class="abs more" style="left:77px;top:725px">Know more...</span>
    <span class="abs more" style="left:304px;top:725px">Know more...</span>
    <span class="abs more" style="left:558px;top:722px">Know more...</span>

    <h2 class="abs sec" style="left:76px;top:789px">JUST LOOK OUR BEST REAL ESTATE DEALS</h2>
    <div class="abs rule" style="left:76px;top:812px;width:432px"></div>

    <div class="abs deal" style="left:77px;top:824px"><div class="img" role="img" aria-label="Single-storey house with lawn"></div><div class="price">Rent : <b>$270</b> / month</div><div class="spec">3 Bedrooms<br>1 Bathrooms</div><div class="more">More Details...</div></div>
    <div class="abs deal" style="left:190px;top:824px"><div class="img" role="img" aria-label="Brick house with garage"></div><div class="price">Rent : <b>$400</b> / month</div><div class="spec">3 Bedrooms<br>1 Bathrooms</div><div class="more">More Details...</div></div>
    <div class="abs deal" style="left:303px;top:824px"><div class="img" role="img" aria-label="Red brick home"></div><div class="price">Rent : <b>$300</b> / month</div><div class="spec">3 Bedrooms<br>1 Bathrooms</div><div class="more">More Details...</div></div>
    <div class="abs deal" style="left:417px;top:824px"><div class="img" role="img" aria-label="Modern rendered home"></div><div class="price">Rent : <b>$350</b> / month</div><div class="spec">3 Bedrooms<br>1 Bathrooms</div><div class="more">More Details...</div></div>

    <h2 class="abs sec" style="left:541px;top:789px">TESTIMONIALS</h2>
    <div class="abs rule" style="left:541px;top:812px;width:194px"></div>
    <div class="abs" style="left:540px;top:822px;font:12px Arimo,sans-serif">What our customers think</div>
    <p class="abs quote" style="left:540px;top:850px">The experience of finding a rental was excellent and the staff were very professional and I couldn't have asked for more.</p>
    <span class="abs by" style="left:541px;top:887px">by Tom R.</span>
    <div class="abs rule" style="left:540px;top:904px;width:194px;background:#ddd"></div>
    <p class="abs quote" style="left:540px;top:912px">Brightkey Homes Management have been managing my property for over two years and have always provided an excellent service.</p>
    <span class="abs by" style="left:541px;top:950px">by Daniel Okoro</span>

    <div class="abs" style="left:537px;top:995px;font:12px Arimo,sans-serif">Brightkey Homes Management</div>
    <div class="abs" style="left:537px;top:1011px;font:9px Arimo,sans-serif;color:#7a9cc6">Rated: 5 Stars By 10 Users</div>
    <div class="abs stars" style="left:537px;top:1023px"><i></i><i></i><i></i><i></i><i></i></div>
  </main>

  <section>
    <div class="abs feat-tab">Featured Properties</div>
    <div class="abs feat"></div>
    <div class="abs arrow" style="left:51px;top:1075px"><svg width="8" height="10"><path d="M7 0L0 5l7 5z" fill="#fff"/></svg></div>
    <div class="abs arrow" style="left:728px;top:1075px"><svg width="8" height="10"><path d="M1 0l7 5-7 5z" fill="#fff"/></svg></div>

    <div class="abs" style="left:78px;top:1054px"><div class="thumb" role="img" aria-label="Family home with palm trees"></div><div class="tcap">Family home in Westbrook<br>with Large Shed</div></div>
    <div class="abs" style="left:186px;top:1054px"><div class="thumb" role="img" aria-label="Family home with palm trees"></div><div class="tcap">Family home in Westbrook<br>with Large Shed</div></div>
    <div class="abs" style="left:297px;top:1054px"><div class="thumb" role="img" aria-label="Family home with palm trees"></div><div class="tcap">Family home in Westbrook<br>with Large Shed</div></div>
    <div class="abs" style="left:408px;top:1054px"><div class="thumb" role="img" aria-label="Family home with palm trees"></div><div class="tcap">Family home in Westbrook<br>with Large Shed</div></div>
    <div class="abs" style="left:519px;top:1054px"><div class="thumb" role="img" aria-label="Family home with palm trees"></div><div class="tcap">Family home in Westbrook<br>with Large Shed</div></div>
    <div class="abs" style="left:631px;top:1054px"><div class="thumb" role="img" aria-label="Family home with palm trees"></div><div class="tcap">Family home in Westbrook<br>with Large Shed</div></div>
    <div class="abs call">Call Us Now 08 - 5550 - 1234</div>
  </section>

  <footer>
    <div class="abs footer" role="img" aria-label="Faint city skyline backdrop"></div>
    <div class="abs fcol" style="left:72px;top:1206px;width:150px"><h4>About Real Homes</h4><p>You'll find just what you need with Brightkey Homes Management. Not only do we offer a completely unparalleled range of properties and locations, we're also the first choice for property owners looking for a singularly dedicated property management specialist. More...</p></div>
    <div class="abs fcol" style="left:244px;top:1206px"><h4>Quick Links</h4><p>Frequently asked Questions<br>How do I pay rent?<br>Tenant Policies<br>Tenants Information</p></div>
    <div class="abs fcol" style="left:415px;top:1206px"><h4>Quick Links</h4><p>Newsletter<br>Legal Information<br>Sitemap</p></div>
    <div class="abs fcol" style="left:586px;top:1206px"><h4>Contact Info</h4><p>First Floor<br>42 Harbour Lane<br>Coralton WA 6000</p></div>
    <div class="abs fline"></div>
    <div class="abs copy" style="left:62px;top:1348px">© 2013 All Rights Reserved by Brightkey Homes</div>
    <div class="abs copy" style="left:638px;top:1348px">Powered by <span style="color:#999">Northlane Studio</span></div>
  </footer>
</div>
</body>
</html>
```